Seasoned logs and kindling for sale

producing firewood from beech,ash,oak and silver birch,
Kindling is produce from a variety of seasoned softwoods

Industry/Entity Type

Firewood

Contact Information for Business Card

mark Pellew 07812603948
dave Tillard 07846217035
e-mail,markp318@mailbrook.net

```html
<!DOCTYPE html>
<html lang="en">
<head>
<meta charset="utf-8">
<title>Seasoned Logs and Kindling for Sale – Business Card</title>
<link href="https://fonts.googleapis.com/css2?family=Black+Ops+One&family=Arimo:wght@700&display=swap" rel="stylesheet">
<style>
  :root {
    --page-bg: #ffffff;
    --log-light: #d9b27a;
    --log-mid: #a8773f;
    --log-dark: #5a3a1c;
    --title-fill: #9a5a22;
    --title-edge: #1c1108;
    --band-light: #f2f4f5;
    --band-mid: #b9bdc0;
    --band-dark: #6f7376;
    --wood-light: #a86a2c;
    --wood-mid: #7a4a1e;
    --wood-dark: #3f240e;
    --silver-top: #ffffff;
    --silver-bottom: #8e9194;
    --text-shadow: #2a1709;
  }
  html, body {
    margin: 0;
    padding: 0;
    width: 1200px;
    height: 900px;
    overflow: hidden;
    background: var(--page-bg);
  }
  .canvas {
    position: relative;
    width: 1200px;
    height: 900px;
  }
  .card {
    position: absolute;
    left: 143px;
    top: 105px;
    width: 922px;
    height: 588px;
    overflow: hidden;
    box-shadow: 0 0 8px rgba(0,0,0,0.35);
  }
  .log-stack {
    position: absolute;
    left: 0; top: 0;
    width: 922px; height: 252px;
    background:
      radial-gradient(ellipse at 20% 30%, var(--log-light) 0%, transparent 45%),
      radial-gradient(ellipse at 75% 70%, var(--log-light) 0%, transparent 45%),
      linear-gradient(160deg, var(--log-mid) 0%, var(--log-light) 40%, var(--log-mid) 70%, var(--log-dark) 100%);
  }
  .headline {
    position: absolute;
    left: 0; top: 62px;
    width: 922px;
    margin: 0;
    text-align: center;
    font-family: "Black Ops One", "Arial Black", sans-serif;
    font-weight: 400;
    font-size: 76px;
    line-height: 86px;
    letter-spacing: 4px;
    color: var(--title-fill);
    -webkit-text-stroke: 3px var(--title-edge);
    paint-order: stroke fill;
    text-shadow: 3px 4px 0 var(--title-edge);
    text-transform: uppercase;
  }
  .steel-band {
    position: absolute;
    left: 0; top: 252px;
    width: 922px; height: 25px;
    background: linear-gradient(90deg, var(--band-dark) 0%, var(--band-mid) 20%, var(--band-light) 50%, var(--band-mid) 80%, var(--band-dark) 100%);
  }
  .wood-panel {
    position: absolute;
    left: 0; top: 277px;
    width: 922px; height: 311px;
    background:
      radial-gradient(ellipse at 45% 75%, var(--wood-light) 0%, transparent 40%),
      radial-gradient(ellipse at 80% 60%, rgba(168,106,44,0.6) 0%, transparent 35%),
      linear-gradient(90deg, var(--wood-dark) 0%, var(--wood-mid) 30%, var(--wood-light) 55%, var(--wood-mid) 80%, var(--wood-dark) 100%);
  }
  .contact {
    position: absolute;
    margin: 0;
    font-family: "Arimo", Arial, sans-serif;
    font-weight: 700;
    white-space: nowrap;
    background: linear-gradient(180deg, var(--silver-top) 0%, var(--silver-bottom) 100%);
    -webkit-background-clip: text;
    background-clip: text;
    color: transparent;
    filter: drop-shadow(2px 2px 1px var(--text-shadow)) drop-shadow(-1px -1px 0 var(--text-shadow));
  }
  .contact-name { font-size: 50px; line-height: 56px; }
  .contact-phone { font-size: 43px; line-height: 48px; letter-spacing: 1px; }
  .contact-email { font-size: 33px; line-height: 40px; }
  .left { left: 17px; }
  .right { right: 15px; text-align: right; }
  .name-row { top: 335px; }
  .phone-row { top: 395px; }
  .contact-email { left: 0; width: 922px; text-align: center; top: 505px; }
</style>
</head>
<body>
<main class="canvas">
  <section class="card">
    <div class="log-stack" role="img" aria-label="Photograph of a stack of split seasoned firewood logs"></div>
    <h1 class="headline">Seasoned logs and<br>kindling for sale</h1>
    <div class="steel-band"></div>
    <div class="wood-panel" role="img" aria-label="Photograph of weathered brown wooden planks"></div>

    <p class="contact contact-name left name-row">Mark Pellew</p>
    <p class="contact contact-phone left phone-row">07812603948</p>
    <p class="contact contact-name right name-row">Dave Tillard</p>
    <p class="contact contact-phone right phone-row">07846217035</p>
    <p class="contact contact-email">markp318@mailbrook.net</p>
  </section>
</main>
</body>
</html>
```